Kestrel Signs Facebook Banner Design

Design a facebook banner for a sign company. I would like to have a modern approach to it.

Product Offering:
Signs
Banners
Decals
Commercial Wraps

```html
<!DOCTYPE html>
<html lang="en">
<head>
<meta charset="utf-8">
<title>Kestrel Signs – Facebook Banner Concepts</title>
<link rel="stylesheet" href="https://fonts.googleapis.com/css2?family=Barlow:wght@600;700;800&family=Roboto:wght@400;700&display=swap">
<style>
  :root {
    --board: #c6c6c6;
    --charcoal: #48484a;
    --red: #e8363c;
    --white: #ffffff;
    --shadow: rgba(0,0,0,0.18);
  }
  * { margin: 0; padding: 0; box-sizing: border-box; }
  html, body { width: 1200px; height: 1022px; overflow: hidden; }
  body { background: var(--board); position: relative; font-family: "Roboto", Arial, sans-serif; color: var(--white); }

  .banner {
    position: absolute; left: 88px; width: 1025px; height: 380px;
    background: var(--charcoal); overflow: hidden;
    box-shadow: 0 6px 18px var(--shadow);
  }
  .banner--wave { top: 84px; }
  .banner--tiles { top: 559px; }
  .banner svg.shapes { position: absolute; inset: 0; width: 1025px; height: 380px; }
  .abs { position: absolute; }

  .headline { font-family: "Barlow", Arial, sans-serif; font-weight: 700; text-transform: uppercase; line-height: 1; }
  .wave-heading { left: 42px; top: 32px; font-size: 22px; letter-spacing: 0.2px; }

  .service { display: flex; align-items: center; gap: 13px; }
  .service-icon { width: 56px; height: 56px; border-radius: 50%; background: var(--red); display: flex; align-items: center; justify-content: center; flex: none; }
  .service-name { font-weight: 700; font-size: 18px; line-height: 1.2; }

  .brand-name { font-family: "Barlow", Arial, sans-serif; font-weight: 800; color: var(--red); text-transform: uppercase; text-align: center; line-height: 0.95; }
  .wave-brand { left: 174px; top: 292px; width: 246px; font-size: 34px; }

  .wave-phone { right: 10px; top: 258px; font-weight: 700; font-size: 20px; }
  .wave-web { right: 12px; top: 295px; font-weight: 700; font-size: 14px; }

  .tiles-brand { left: 20px; top: 48px; width: 200px; font-size: 25px; text-align: left; }
  .tiles-heading { left: 41px; top: 150px; font-size: 28px; line-height: 1.3; }
  .call { left: 41px; top: 253px; display: flex; align-items: center; gap: 13px; }
  .call-icon { width: 40px; height: 40px; border-radius: 50%; background: var(--white); display: flex; align-items: center; justify-content: center; }
  .call-label { font-size: 14px; }
  .call-number { font-family: "Barlow", Arial, sans-serif; font-weight: 700; font-size: 24px; line-height: 1.1; }

  .tile-label { font-weight: 700; font-size: 18px; text-align: center; width: 240px; line-height: 1; }
</style>
</head>
<body>

<!-- Concept one: curved photo banner -->
<section class="banner banner--wave">
  <svg class="shapes" viewBox="0 0 1025 380" aria-hidden="false">
    <defs>
      <linearGradient id="officeTone" x1="0" y1="0" x2="1" y2="1">
        <stop offset="0" stop-color="#eeebe6"/>
        <stop offset="0.55" stop-color="#cfc9bf"/>
        <stop offset="1" stop-color="#8f8a82"/>
      </linearGradient>
    </defs>
    <path class="accent-arc" d="M440,0 Q395,200 560,380 L600,380 Q440,200 500,0 Z" fill="var(--red)"/>
    <path class="accent-arc-inner" d="M500,0 Q440,200 600,380 L625,380 Q462,200 520,0 Z" fill="var(--white)"/>
    <path class="photo-area" role="img" aria-label="Photo of a smiling designer sketching on a tablet at a laptop in a bright office" d="M520,0 L1025,0 L1025,380 L625,380 Q462,200 520,0 Z" fill="url(#officeTone)"/>
    <path class="contact-edge" d="M670,380 C810,372 835,240 925,222 Q985,208 1025,212 L1025,380 Z" fill="var(--red)"/>
    <path class="contact-panel" d="M700,380 C830,378 850,252 935,236 Q990,226 1025,230 L1025,380 Z" fill="var(--charcoal)"/>
    <path class="base-edge" d="M0,295 Q270,200 560,340 L560,380 L0,380 Z" fill="var(--red)"/>
    <path class="base-wave" d="M0,350 Q260,215 600,380 L0,380 Z" fill="var(--white)"/>
  </svg>

  <h1 class="abs headline wave-heading">Transform your brand with</h1>

  <div class="abs service" style="left:42px; top:85px;">
    <span class="service-icon">
      <svg width="32" height="32" viewBox="0 0 32 32" fill="none" stroke="#fff" stroke-width="2"><circle cx="16" cy="16" r="13"/><rect x="10" y="10" width="12" height="9" rx="1"/><path d="M16 19v6M6 26L26 6"/></svg>
    </span>
    <span class="service-name">Signs</span>
  </div>
  <div class="abs service" style="left:217px; top:85px;">
    <span class="service-icon">
      <svg width="32" height="32" viewBox="0 0 32 32" fill="none" stroke="#fff" stroke-width="2"><rect x="4" y="6" width="24" height="20" rx="1"/><path d="M4 11h24"/><rect x="9" y="15" width="14" height="7"/></svg>
    </span>
    <span class="service-name">Banners</span>
  </div>
  <div class="abs service" style="left:42px; top:160px;">
    <span class="service-icon">
      <svg width="32" height="32" viewBox="0 0 32 32" fill="none" stroke="#fff" stroke-width="2"><path d="M16 4a12 12 0 1 0 12 12L16 28"/><path d="M28 16c-7 0-12 5-12 12"/><path d="M10 12a7 7 0 0 1 8-4"/></svg>
    </span>
    <span class="service-name">Decals</span>
  </div>
  <div class="abs service" style="left:217px; top:160px;">
    <span class="service-icon">
      <svg width="34" height="34" viewBox="0 0 34 34" fill="none" stroke="#fff" stroke-width="2"><path d="M3 23V10h18l6 6 4 2v5z"/><path d="M21 10v7h8"/><circle cx="10" cy="24" r="3"/><circle cx="25" cy="24" r="3"/></svg>
    </span>
    <span class="service-name">Commercial<br>Wraps</span>
  </div>

  <div class="abs brand-name wave-brand">Kestrel<br>Signs</div>

  <div class="abs wave-phone">(604) 555-0148</div>
  <div class="abs wave-web">www.kestrelsigns.ca/</div>
</section>

<!-- Concept two: angled tile banner -->
<section class="banner banner--tiles">
  <svg class="shapes" viewBox="0 0 1025 380">
    <defs>
      <linearGradient id="storefrontTone" x1="0" y1="0" x2="1" y2="1">
        <stop offset="0" stop-color="#6e5844"/><stop offset="1" stop-color="#46503e"/>
      </linearGradient>
      <linearGradient id="skyTone" x1="0" y1="0" x2="0" y2="1">
        <stop offset="0" stop-color="#2f74cc"/><stop offset="1" stop-color="#a8c8ef"/>
      </linearGradient>
      <linearGradient id="windowTone" x1="0" y1="0" x2="1" y2="1">
        <stop offset="0" stop-color="#1b3540"/><stop offset="1" stop-color="#2e4f52"/>
      </linearGradient>
      <linearGradient id="vanTone" x1="0" y1="0" x2="1" y2="0">
        <stop offset="0" stop-color="#e6e8ea"/><stop offset="1" stop-color="#c7ccd0"/>
      </linearGradient>
    </defs>
    <polygon class="hero-panel" points="0,0 298,0 464,188 300,380 0,380" fill="var(--red)"/>
    <polygon class="brand-tab" points="0,34 227,34 280,101 0,101" fill="var(--white)"/>

    <polygon class="tile-photo" role="img" aria-label="Photo of a projecting storefront sign on a brick wall" points="373,19 620,19 723,147 478,147" fill="url(#storefrontTone)" stroke="#fff" stroke-width="3"/>
    <polygon class="tile-bar" points="478,151 723,151 746,179 501,179" fill="var(--red)"/>

    <polygon class="tile-photo" role="img" aria-label="Photo of a lodge roadside sign against a blue sky" points="641,19 990,19 990,147 743,147" fill="url(#skyTone)" stroke="#fff" stroke-width="3"/>
    <polygon class="tile-bar" points="743,151 990,151 1013,179 766,179" fill="var(--red)"/>

    <polygon class="tile-photo" role="img" aria-label="Photo of seasonal window decals on glass" points="478,210 737,210 635,340 384,340" fill="url(#windowTone)" stroke="#fff" stroke-width="3"/>
    <polygon class="tile-bar" points="384,344 635,344 612,372 361,372" fill="var(--red)"/>

    <polygon class="tile-photo" role="img" aria-label="Photo of a cargo van with a full printed wrap" points="755,210 1002,210 900,340 649,340" fill="url(#vanTone)" stroke="#fff" stroke-width="3"/>
    <polygon class="tile-bar" points="649,344 900,344 877,372 626,372" fill="var(--red)"/>
  </svg>

  <div class="abs brand-name tiles-brand">Kestrel<br>Signs</div>

  <h2 class="abs headline tiles-heading">Transform your<br>brand with</h2>

  <div class="abs call">
    <span class="call-icon">
      <svg width="20" height="20" viewBox="0 0 24 24" fill="var(--red)"><path d="M6.6 10.8a15.1 15.1 0 0 0 6.6 6.6l2.2-2.2a1 1 0 0 1 1-.25 11.4 11.4 0 0 0 3.6.57 1 1 0 0 1 1 1V20a1 1 0 0 1-1 1A17 17 0 0 1 3 4a1 1 0 0 1 1-1h3.5a1 1 0 0 1 1 1c0 1.25.2 2.45.57 3.57a1 1 0 0 1-.25 1z"/></svg>
    </span>
    <span>
      <span class="call-label">Call Us Today</span><br>
      <span class="call-number">(604) 555-0148</span>
    </span>
  </div>

  <div class="abs tile-label" style="left:492px; top:156px;">Signs</div>
  <div class="abs tile-label" style="left:758px; top:156px;">Banners</div>
  <div class="abs tile-label" style="left:378px; top:349px;">Decal</div>
  <div class="abs tile-label" style="left:643px; top:349px;">Commercial Wraps</div>
</section>

</body>
</html>
```